Food Label: GlenoraSip - IMO - Isomalto-oligosaccharides syrup

GlenoraSip is a thick, syrupy liquid soluble pre-biotic fiber.

It is pure, Isomalto-oligosaccharides made from tapioca starch.

It is has nice sweet flavor and serves as a super low sugar alternative sweetener. It is being sold as an ingredient.

It is a key ingredient in wildly popular Lumen Bars.

It is gluten free, kosher, vegan, non-GMO. It is made from Tapioca Starch.

We need a product logo and a label concept.

Use color but not too many colors. Must reproduce well in greyscale.

Start by submitting logo. Finish by submitting complete labels in 2 sizes:

4" h x 6" w and 2.5 h x 4" w

The winning designer will be required to make 3 print ready labels (in 2 sizes) for 3 different sized containers of this product. At that point we will provide required text, nutritional info and UPCs.

GOOD LUCK!

Target Market(s)

Health conscious consumers making their own concoctions at home. Mostly for general health. Some due to digestive/intestinal medical conditions.

Industry/Entity Type

Product

Requirements
Must have
• Distinct clear promient product name.
Nice to have
• Great surrounding aesthetic for the entire label/package.
Should not have
• Hard to read font. Extraneous detailed graphic elements.

```html
<!DOCTYPE html>
<html lang="en">
<head>
<meta charset="utf-8">
<title>GlenoraSip IMO Syrup Label</title>
<link rel="stylesheet" href="https://fonts.googleapis.com/css2?family=Montserrat:wght@400;500;600;700&display=swap">
<style>
  :root {
    --page-bg: #ececec;
    --label-light: #dbe5ee;
    --label-mid: #b7c9d8;
    --ink-dark: #333b44;
    --ink-brand: #5d6670;
    --ink-body: #3f4750;
    --band: #6e7c89;
    --band-text: #eef2f5;
  }
  * { margin: 0; padding: 0; box-sizing: border-box; }
  html, body { width: 1200px; height: 900px; overflow: hidden; }
  body {
    background: var(--page-bg);
    font-family: "Montserrat", sans-serif;
    position: relative;
  }
  .label {
    position: absolute;
    left: 150px;
    top: 150px;
    width: 900px;
    height: 600px;
    overflow: hidden;
  }
  .label-texture {
    position: absolute;
    inset: 0;
    background: radial-gradient(ellipse at 50% 40%, var(--label-light) 0%, var(--label-mid) 100%);
  }
  .label-content { position: relative; height: 100%; }
  .brand {
    position: absolute;
    top: 40px;
    left: 0; right: 0;
    text-align: center;
    font-size: 54px;
    font-weight: 600;
    color: var(--ink-brand);
    letter-spacing: -0.5px;
  }
  .product-name {
    position: absolute;
    top: 128px;
    left: 0; right: 0;
    text-align: center;
    font-weight: 600;
    color: var(--ink-dark);
    line-height: 1;
  }
  .product-name .line-one { display: block; font-size: 84px; letter-spacing: -1px; }
  .product-name .line-two { display: block; font-size: 40px; margin-top: 12px; letter-spacing: -0.5px; }
  .intro {
    position: absolute;
    top: 288px;
    left: 90px; right: 90px;
    text-align: center;
    font-size: 17px;
    line-height: 1.4;
    color: var(--ink-body);
  }
  .details {
    position: absolute;
    top: 366px;
    left: 90px;
    width: 380px;
    font-size: 18px;
    line-height: 1.4;
    color: var(--ink-body);
  }
  .details strong { font-weight: 700; color: var(--ink-dark); }
  .details p + p { margin-top: 10px; }
  .claims {
    position: absolute;
    top: 362px;
    left: 540px;
    list-style: none;
    font-size: 30px;
    font-weight: 600;
    line-height: 1.25;
    color: var(--ink-dark);
  }
  .bottom-band {
    position: absolute;
    left: 0; right: 0;
    bottom: 0;
    height: 60px;
    background: var(--band);
    color: var(--band-text);
    font-size: 16px;
    font-weight: 600;
    letter-spacing: 0.6px;
    white-space: nowrap;
    line-height: 60px;
    text-align: center;
  }
</style>
</head>
<body>
  <section class="label">
    <div class="label-texture" role="img" aria-label="Faint light blue line pattern behind the label text"></div>
    <div class="label-content">
      <div class="brand">GlenoraSip</div>
      <h1 class="product-name">
        <span class="line-one">IMO SYRUP</span>
        <span class="line-two">ISOMALTO-OLIGOSACCHARIDES</span>
      </h1>
      <p class="intro">
        A thick, syrupy soluble prebiotic fiber with a naturally sweet flavor.
        A super low sugar alternative sweetener for your own recipes and concoctions at home.
      </p>
      <div class="details">
        <p>Pure isomalto-oligosaccharides made from tapioca starch. <strong>Soluble prebiotic fiber for everyday health.</strong></p>
        <p>Net contents<br><strong>16 fl oz (473 mL)</strong></p>
      </div>
      <ul class="claims">
        <li>Gluten free</li>
        <li>Kosher</li>
        <li>Vegan</li>
        <li>Non-GMO</li>
      </ul>
      <div class="bottom-band">SOLUBLE PREBIOTIC FIBER &middot; LOW SUGAR SWEETENER &middot; MADE FROM TAPIOCA STARCH</div>
    </div>
  </section>
</body>
</html>
```